Flyer Design Project

I am opening a yoga studio called Harbourlight Yoga .Pilates. Fitness
and require a flyer that will be letterbox dropped. It will two sided - DL size.100mm × 210mm

The studio will offer Vinyasa Flow Yoga and Mat Pilates classes. We aim to enable people to lead healthier, happier lives through improved strength, flexibility and general well being that regular yoga and pilates practice offers.

We offer group classes, private and semi private sessions in yoga and pilates.

it must have the logo on it- I have uploaded the logo in two versions - not sure what will look the best.

pick up one of the colours from the logo as the background colour.

Side one:
Simple and clean with one side showing logo and address details, website and with simple intro about studio (if it fits)

Location: 1st Floor, 17 Wattlegrove Parade, Kelsmoor, 3287
phone: 0412 908316
www.harbourlightkelsmoor.com.au

OPENING OCTOBER

other side - class descriptions and intro offer for new clients
$20 for 7 days of classes
$99 for 1 month unlimited.

Class descriptions:
Vinyasa Flow yoga: A class that flows from pose to pose integrating breath, alignment, strength and power. All levels are catered for in a warm room heated to around 26 degrees. You will leave feeling inspired, empowered and energised.

Mat Pilates: A strong, challenging class integrating the key principles of pilates: concentration, control, centring, precision, flowing movement and breath. Using the core as a focus to develop these principles you will be hooked on the physical freedom you experience post workout:improved strength, flexibility and vitality that pilates offers.

Private and semi Private tuition available.

Target Market(s)

mainly women, athletic, 35-55 age, middle class, well educated

Industry/Entity Type

Fitness

Requirements
Must have
• 2 pages
the logo

Should not have
• no pics

```html
<!DOCTYPE html>
<html lang="en">
<head>
<meta charset="utf-8">
<title>Harbourlight Yoga .Pilates. Fitness – DL Flyer</title>
<link rel="stylesheet" href="https://fonts.googleapis.com/css2?family=Arimo:wght@400;700&display=swap">
<style>
  :root {
    --orange: #f08f1c;
    --yellow: #fbd41b;
    --blue: #0ab4e6;
    --red: #e3222b;
    --ink: #1d2932;
    --white: #ffffff;
    --backdrop: #e8e4dd;
    --photo-dark: #4a3a22;
    --photo-mid: #8a7446;
    --photo-light: #c9b58a;
  }
  * { box-sizing: border-box; margin: 0; padding: 0; }
  html, body { width: 1200px; height: 960px; overflow: hidden; }
  body {
    background: var(--backdrop);
    font-family: "Arimo", Arial, sans-serif;
    color: var(--ink);
    position: relative;
  }
  .flyer-side {
    position: absolute;
    left: 152px;
    width: 898px;
    height: 427px;
    overflow: hidden;
    box-shadow: 0 3px 10px rgba(0,0,0,.25);
  }
  .side-front { top: 37px; }
  .side-back { top: 507px; }

  .panel { position: absolute; }
  .panel-warm { background: radial-gradient(ellipse at 50% 50%, var(--yellow) 0%, #f8bb1c 45%, var(--orange) 100%); }
  .panel-blue { background: var(--blue); }
  .divider { position: absolute; left: 465px; top: 0; width: 4px; height: 100%; background: var(--red); }

  /* front side */
  .brand-panel { left: 0; top: 0; width: 465px; height: 215px; }
  .brand {
    position: absolute; left: 0; right: 0; top: 62px;
    display: flex; flex-direction: column; align-items: center; gap: 14px;
  }
  .brand-dot { width: 74px; height: 74px; border-radius: 50%; background: var(--white); opacity: .9; }
  .brand-name { font-size: 22px; font-weight: 700; color: #55575a; letter-spacing: .5px; }
  .intro-panel { left: 0; top: 215px; width: 465px; height: 212px; border-top: 3px solid #2a8fc0; }
  .ticks { position: absolute; left: 18px; top: 12px; width: 444px; list-style: none; }
  .ticks li {
    position: relative; padding-left: 22px; font-size: 14.5px; line-height: 19.7px;
    text-align: justify; margin-bottom: 13px;
  }
  .ticks svg { position: absolute; left: 0; top: 4px; }
  .contact { position: absolute; left: 40px; top: 143px; font-size: 13px; line-height: 16.6px; }
  .contact svg { vertical-align: -1px; margin-right: 3px; }
  .contact .gap { margin-left: 10px; }
  .photo-area {
    left: 469px; top: 0; width: 429px; height: 427px;
    background: linear-gradient(180deg, var(--photo-light) 0%, var(--photo-mid) 40%, var(--photo-dark) 75%, var(--photo-mid) 100%);
  }
  .opening { position: absolute; left: 489px; top: 392px; font-size: 23px; font-weight: 700; color: var(--white); letter-spacing: .3px; }

  /* back side */
  .offer-panel { left: 0; top: 0; width: 465px; height: 217px; }
  .aim { position: absolute; left: 33px; top: 25px; width: 406px; font-size: 14.5px; line-height: 20.5px; text-align: justify; }
  .new-clients { position: absolute; left: 33px; top: 112px; font-size: 30px; font-weight: 700; color: var(--red); }
  .prices { position: absolute; left: 33px; top: 152px; font-size: 24px; line-height: 26px; }
  .offer-dot { position: absolute; left: 360px; top: 100px; width: 72px; height: 72px; border-radius: 50%; background: var(--white); opacity: .85; }
  .classes-panel { left: 0; top: 217px; width: 465px; height: 210px; }
  .pilates-panel { left: 469px; top: 0; width: 429px; height: 217px; }
  .run-panel { left: 469px; top: 217px; width: 429px; height: 210px; }
  .section-title { position: absolute; font-size: 30px; font-weight: 400; }
  .class-name { font-size: 23px; font-weight: 400; margin-bottom: 4px; }
  .class-text { font-size: 16px; line-height: 22.5px; text-align: justify; }
  .class-block { position: absolute; }
  .classes-panel .section-title { left: 41px; top: 10px; }
  .classes-panel .class-block { left: 43px; top: 50px; width: 392px; }
  .pilates-panel .class-block { left: 24px; top: 38px; width: 366px; }
  .run-panel .class-block { left: 24px; top: 17px; width: 366px; }
</style>
</head>
<body>

<section class="flyer-side side-front">
  <div class="panel panel-warm brand-panel">
    <div class="brand">
      <span class="brand-dot"></span>
      <span class="brand-name">Harbourlight Yoga .Pilates. Fitness</span>
    </div>
  </div>

  <div class="panel panel-blue intro-panel">
    <ul class="ticks">
      <li><svg width="16" height="14" viewBox="0 0 16 14"><path d="M1 8 L5 12 L15 1" fill="none" stroke="#e3222b" stroke-width="2.4"/></svg>We offer Vinyasa Flow Yoga, Mat Pilates classes and running groups to help you become the healthiest and happiest version of yourself you can be.</li>
      <li><svg width="16" height="14" viewBox="0 0 16 14"><path d="M1 8 L5 12 L15 1" fill="none" stroke="#e3222b" stroke-width="2.4"/></svg>Private and semi private sessions available in yoga and pilates.</li>
    </ul>
    <div class="contact">
      <p>1st Floor, 17 Wattlegrove Parade, Kelsmoor, 3287</p>
      <p><svg width="10" height="10" viewBox="0 0 10 10"><circle cx="5" cy="5" r="4.5" fill="#fff"/><path d="M3 2.5 Q3 7 7.5 7.5" stroke="#0ab4e6" stroke-width="1.4" fill="none"/></svg>0412 908316<span class="gap"><svg width="11" height="8" viewBox="0 0 11 8"><rect width="11" height="8" fill="#fff"/><path d="M0 0 L5.5 4.5 L11 0" stroke="#0ab4e6" fill="none"/></svg>info@harbourlightkelsmoor.com.au</span></p>
      <p><svg width="10" height="10" viewBox="0 0 10 10"><circle cx="5" cy="5" r="4.5" fill="#fff"/><circle cx="5" cy="5" r="2.2" fill="none" stroke="#0ab4e6" stroke-width="1"/></svg>www.harbourlightkelsmoor.com.au</p>
    </div>
  </div>

  <div class="panel photo-area" role="img" aria-label="Photo of a woman holding a standing yoga pose on a concrete ledge beside water under a bridge"></div>
  <div class="divider"></div>
  <p class="opening">OPENING OCTOBER</p>
</section>

<section class="flyer-side side-back">
  <div class="panel panel-warm offer-panel">
    <p class="aim">We aim to enable people to lead healthier, happier lives through improved strength, flexibility and general well being that regular yoga and Pilates practice offers.</p>
    <p class="new-clients">NEW CLIENTS</p>
    <p class="prices">$20 for 7 days of classes<br>$99 for 1 month unlimited.</p>
    <span class="offer-dot"></span>
  </div>

  <div class="panel panel-blue classes-panel">
    <h2 class="section-title">Class descriptions:</h2>
    <div class="class-block">
      <h3 class="class-name">Vinyasa Flow Yoga:</h3>
      <p class="class-text">A class that flows from pose to pose integrating breath, alignment, strength and power. All levels are catered for in a warm room heated to around 26 degrees. You will leave feeling inspired, empowered and energised.</p>
    </div>
  </div>

  <div class="panel panel-blue pilates-panel">
    <div class="class-block">
      <h3 class="class-name">Mat Pilates:</h3>
      <p class="class-text">A strong, challenging class using the core as a focus and incorporating the principles of pilates including concentration and breath. Get hooked on the physical freedom you experience post workout:improved strength, flexibility and vitality that pilates offers.</p>
    </div>
  </div>

  <div class="panel panel-warm run-panel">
    <div class="class-block">
      <h3 class="class-name">Run Groups:</h3>
      <p class="class-text">Beginners to athletes, join our passion for running in a social, non competitive environment. Run groups are the ideal way to get fit and solve the problems of the world one step at a time. Best of all there is a yoga class waiting for you at the end to dissolve into!</p>
    </div>
  </div>

  <div class="divider"></div>
</section>

</body>
</html>
```